BUSINESS CARD DESIGN

NAME- TODD MASVERIK
PHONE NUMER - 808- 451-7082
EMAIL- OFFICE@VORLINDE-GRADEWAY.COM
BACK OF CARD- SPEACIALIZES IN LAND CLEARING, FORESTRY MUCLHING AND EXCAVATION

Contact Information for Business Card

NAME- TODD MASVERIK PHONE NUMER - 808- 451-7082 EMAIL- OFFICE@VORLINDE-GRADEWAY.COM BACK OF CARD- SPEACIALIZES IN LAND CLEARING , MUCLHING AND EXCAVATION

```html
<!DOCTYPE html>
<html lang="en">
<head>
<meta charset="utf-8">
<title>Todd Masverik – Business Card</title>
<link href="https://fonts.googleapis.com/css2?family=Josefin+Sans:wght@500&family=Montserrat:wght@600;700&display=swap" rel="stylesheet">
<style>
  :root {
    --backdrop: #e9e4dc;
    --card-white: #ffffff;
    --charcoal: #363534;
    --amber: #f5ae4e;
    --amber-deep: #e9962a;
    --amber-text: #f39a1e;
  }
  html, body {
    margin: 0;
    width: 1200px;
    height: 900px;
    overflow: hidden;
    background: var(--backdrop);
  }
  .canvas {
    position: relative;
    width: 1200px;
    height: 900px;
  }
  .card {
    position: absolute;
    left: 250px;
    width: 700px;
    height: 400px;
    overflow: hidden;
    box-shadow: 0 10px 28px rgba(0, 0, 0, 0.18);
  }
  .card--front { top: 30px; background: var(--card-white); }
  .card--back { top: 470px; background: var(--charcoal); }

  .front-corners { position: absolute; inset: 0; }

  .front-panel {
    position: absolute;
    left: 70px;
    top: 60px;
    width: 560px;
    height: 270px;
    background: var(--amber);
    overflow: hidden;
  }
  .ridge-band {
    position: absolute;
    left: 0;
    right: 0;
    bottom: 0;
    height: 110px;
    background: linear-gradient(180deg, rgba(233, 150, 42, 0.35) 0%, var(--amber-deep) 60%);
  }
  .contact {
    position: absolute;
    right: 40px;
    top: 50px;
    text-align: right;
    color: var(--charcoal);
  }
  .contact__name {
    margin: 0;
    font-family: "Josefin Sans", sans-serif;
    font-weight: 500;
    font-size: 46px;
    letter-spacing: 2px;
  }
  .contact__phone {
    margin: 14px 0 0;
    font-family: "Montserrat", sans-serif;
    font-weight: 700;
    font-size: 22px;
    letter-spacing: 2px;
  }
  .contact__email {
    margin: 6px 0 0;
    font-family: "Montserrat", sans-serif;
    font-weight: 600;
    font-size: 12px;
    letter-spacing: 1.4px;
  }

  .specialty {
    position: absolute;
    left: 90px;
    top: 130px;
    margin: 0;
    color: var(--amber-text);
    font-family: "Montserrat", sans-serif;
    font-weight: 700;
    font-size: 19px;
    letter-spacing: 2.2px;
    line-height: 1.35;
    text-align: center;
  }
  .shard-area {
    position: absolute;
    left: 80px;
    bottom: 40px;
    width: 540px;
    height: 100px;
    background: linear-gradient(100deg, var(--amber-text) 0%, rgba(243, 154, 30, 0.55) 60%, rgba(243, 154, 30, 0.15) 100%);
  }
</style>
</head>
<body>
<main class="canvas">
  <section class="card card--front" aria-label="Card front">
    <svg class="front-corners" width="700" height="400" viewBox="0 0 700 400" aria-hidden="true">
      <polygon points="0,345 110,175 600,175 650,0 700,0 700,400 0,400" fill="var(--charcoal)"/>
    </svg>
    <div class="front-panel">
      <div class="ridge-band" role="img" aria-label="Mountain ridge silhouette in deeper amber"></div>
      <div class="contact">
        <h1 class="contact__name">TODD MASVERIK</h1>
        <p class="contact__phone">808- 451-7082</p>
        <p class="contact__email">OFFICE@VORLINDE-GRADEWAY.COM</p>
      </div>
    </div>
  </section>

  <section class="card card--back" aria-label="Card back">
    <p class="specialty">SPEACIALIZES IN LAND CLEARING,<br>MUCLHING AND EXCAVATION</p>
    <div class="shard-area" role="img" aria-label="Angular amber terrain fragments"></div>
  </section>
</main>
</body>
</html>
```